Brava Stone Oven Kitchen (restaurant)

Restaurant with a cool vibe.
We need a refresh of existing site. Appealing to a hip crowd of 25 or older age bracket (mid price to high small town). Constant changes food and cocktail menu. A vibing atmosphere with jazz funk hip music.
Must be able to scale for any device… phone/mobile device super important.
Instagram: @Brava.Linwell
Website: bravalinwell.example

Target Market(s)

25-55 age group

Number of Pages Required

1 page

Font styles to use
Sans Serif

Requirements
Must have
• Simple to navigate. Simplicity is the key to all sophistication.

Links/Buttons
Menu
Gift Cards
Reservations
Take Out
Contact Us
Should not have
• Please, nothing generic looking… no cookie cutter look. Originality

```html
<!DOCTYPE html>
<html lang="en">
<head>
<meta charset="utf-8">
<title>Brava Stone Oven Kitchen</title>
<link href="https://fonts.googleapis.com/css2?family=Poppins:wght@400;500;600;700&display=swap" rel="stylesheet">
<style>
:root{
  --yellow:#fcd22c;
  --ink:#111;
  --text:#444;
  --muted:#777;
  --light:#f1f1f1;
  --white:#fff;
  --black:#000;
}
*{margin:0;padding:0;box-sizing:border-box}
html,body{width:1200px;height:3403px;overflow:hidden}
body{position:relative;font-family:'Poppins',sans-serif;color:var(--ink);background:var(--white)}
.abs{position:absolute}
.hero-bg{left:0;top:0;width:1200px;height:720px;background:linear-gradient(180deg,#ececec 0%,#f4f4f4 70%,#fff 100%)}
.logo{left:88px;top:20px;line-height:1;text-align:center}
.logo b{display:block;font-size:33px;font-weight:700;letter-spacing:1px}
.logo span{display:block;font-size:11px;font-weight:500;margin-top:2px}
.nav{right:90px;top:30px;display:flex;align-items:center;gap:24px;font-size:13px;font-weight:500}
.nav a{color:var(--ink);text-decoration:none}
.nav .contact{border:2px solid var(--yellow);border-radius:20px;padding:5px 22px}
.food{border-radius:50%}
.hero-title{left:0;width:1200px;top:188px;text-align:center;font-size:57px;font-weight:700;line-height:58px}
.actions{left:382px;top:329px;display:flex;gap:11px}
.action{width:138px;height:137px;background:var(--white);border-radius:3px;box-shadow:0 6px 20px rgba(0,0,0,.06);display:flex;flex-direction:column;align-items:center;justify-content:flex-end;padding-bottom:20px;font-size:14px;font-weight:500}
.action svg{margin-bottom:14px}
.action.active{background:var(--yellow)}
.resbar{left:88px;top:571px;width:1022px;height:98px;background:var(--white);border-radius:49px;box-shadow:0 14px 36px rgba(0,0,0,.08);display:flex;align-items:center;padding:0 38px 0 52px}
.resbar h2{font-size:31px;font-weight:700;width:272px}
.field{font-size:13px;font-weight:600;line-height:18px;position:relative}
.field small{display:block;color:#aaa;font-size:17px;font-weight:400;line-height:20px}
.find{margin-left:auto;background:var(--yellow);border-radius:20px;padding:8px 22px;font-size:13px;font-weight:700;letter-spacing:.5px}
.story-img{left:0;top:748px;width:472px;height:442px}
.story{left:560px;width:466px;top:835px;text-align:center}
.story .kicker{font-size:22px;font-weight:600;color:#999;letter-spacing:1px}
.story h2{font-size:47px;font-weight:700;line-height:50px}
.bar{display:block;width:58px;height:4px;background:var(--yellow);margin:6px auto 0}
.story p{font-size:15px;line-height:26.8px;color:var(--text);margin-top:16px}
.sign{left:706px;top:1075px;width:180px;height:50px;background:linear-gradient(90deg,#e6e6e6,#cfcfcf);border-radius:25px}
.tile{top:1242px;width:503px;height:311px;border-radius:4px;overflow:hidden}
.tile span{position:absolute;left:52px;bottom:44px;color:var(--white);font-size:38px;font-weight:700}
.section-title{left:0;width:1200px;text-align:center;font-size:47px;font-weight:700;line-height:52px}
.review{top:1778px;width:401px;height:242px;background:var(--white);box-shadow:0 10px 30px rgba(0,0,0,.07);padding:64px 28px 0}
.review p{font-size:14px;line-height:22px;color:var(--text);height:100px}
.review hr{border:0;border-top:1px solid #e5e5e5;margin-bottom:14px}
.review h4{font-size:20px;font-weight:600;line-height:22px}
.review small{font-size:15px;color:var(--muted)}
.stars{position:absolute;right:28px;bottom:22px;color:var(--yellow);font-size:19px;letter-spacing:1px}
.stars i{font-style:normal;color:#f6eaba}
.avatar{top:1742px;width:78px;height:78px;border-radius:50%}
.dots{left:574px;top:2071px;display:flex;gap:8px}
.dots b{width:10px;height:10px;border-radius:50%;border:1.5px solid #999}
.dots b.on{border-color:#111;border-width:2px}
.insta{top:2256px;width:199px;height:199px}
.map{left:0;top:2547px;width:1200px;height:450px;background:linear-gradient(135deg,#eeeeee,#e2e2e2 60%,#ececec)}
.footer-col{top:3104px;font-size:13px;line-height:26px}
.footer-col h3{font-size:18px;font-weight:600;margin-bottom:2px;color:var(--white)}
.footer-col{color:var(--white)}
.flogo{left:88px;top:3180px;color:var(--white);text-align:center;line-height:1}
.flogo b{display:block;font-size:40px;font-weight:700;letter-spacing:2px}
.flogo span{font-size:14px}
.social{display:flex;gap:8px;margin-top:10px}
.social b{width:24px;height:24px;border-radius:50%;border:1px solid #555}
.copy{left:0;width:1200px;top:3371px;text-align:center;color:var(--white);font-size:13px}
.rule{left:88px;top:3356px;width:1022px;height:1px;background:#333}
.totop{left:1137px;top:3338px;width:32px;height:32px;border-radius:50%;background:var(--yellow)}
</style>
</head>
<body>
<div class="abs hero-bg"></div>

<div class="abs food" role="img" aria-label="Fresh tomatoes and peppers" style="left:-20px;top:125px;width:180px;height:280px;border-radius:40%;background:radial-gradient(circle,#e23b2a 0%,#c51f16 45%,rgba(236,236,236,0) 70%)"></div>
<div class="abs food" role="img" aria-label="Bowl of pesto dip" style="left:118px;top:194px;width:140px;height:140px;background:radial-gradient(circle,#9aa55a 0%,#6f7a3a 55%,#222 70%)"></div>
<div class="abs food" role="img" aria-label="Bowl of hummus" style="left:-60px;top:410px;width:210px;height:210px;background:radial-gradient(circle,#c48a3a 0%,#a86d25 55%,#8f969a 70%)"></div>
<div class="abs food" role="img" aria-label="Plate of salad" style="left:893px;top:283px;width:126px;height:126px;background:radial-gradient(circle,#8a9b3a 0%,#b54a2a 45%,#fff 68%)"></div>
<div class="abs food" role="img" aria-label="Pizza in a pan" style="left:1085px;top:146px;width:180px;height:180px;background:radial-gradient(circle,#e7b85a 0%,#c0472d 50%,#222 70%)"></div>
<div class="abs food" role="img" aria-label="Plate of tacos" style="left:1060px;top:350px;width:200px;height:280px;border-radius:45%;background:radial-gradient(circle,#d9a04a 0%,#8a6b3a 55%,#6a6a6a 70%)"></div>

<div class="abs logo"><b>BRAVA</b><span>Stone Oven Kitchen</span></div>
<nav class="abs nav">
  <a href="#">Menu</a><a href="#">Gift Cards</a><a href="#">Reservations</a><a href="#">Take Out</a><a href="#" class="contact">Contact Us</a>
</nav>

<h1 class="abs hero-title">Lets Get Lunch<br>At Brava!</h1>

<div class="abs actions">
  <div class="action">
    <svg width="44" height="56" viewBox="0 0 44 56" fill="none" stroke="#111" stroke-width="2"><rect x="12" y="4" width="24" height="44" rx="3"/><path d="M4 30c0-6 8-10 8-4v14M4 30v14l10 8"/><path d="M20 22l4 4 4-8" stroke="#f2b705"/></svg>
    Order Online</div>
  <div class="action active">
    <svg width="58" height="50" viewBox="0 0 58 50" fill="none" stroke="#111" stroke-width="2"><path d="M4 2v46M4 26h12v22M54 2v46M54 26H42v22M18 14h22M29 14v34M22 48h14M20 2h18v12"/></svg>
    Book A Table</div>
  <div class="action">
    <svg width="54" height="54" viewBox="0 0 54 54" fill="none" stroke="#111" stroke-width="2"><path d="M44 18A20 20 0 1 0 28 46"/><path d="M26 14v14l8 6"/><path d="M44 10v8h-8"/><text x="30" y="48" font-family="Poppins,sans-serif" font-size="18" fill="#f2b705" stroke="none">24</text></svg>
    Hours Contact</div>
</div>

<div class="abs resbar">
  <h2>Reservations</h2>
  <div class="field" style="width:174px"><small>▦ Date</small>Wed, Jul 14, 2021</div>
  <div class="field" style="width:148px"><small>◷ Time</small>Closed<span style="position:absolute;right:0;top:16px">⌄</span></div>
  <div class="field" style="width:146px;margin-left:14px"><small>♙ Party Size</small>04<span style="position:absolute;right:0;top:16px">⌄</span></div>
  <div class="find">FIND A TABLE</div>
</div>

<svg class="abs story-img" viewBox="0 0 472 442" role="img" aria-label="Restaurant interior with open kitchen">
  <path d="M0 70 C120 20 260 -10 330 20 C470 80 500 330 380 420 C300 470 200 420 120 380 C70 360 20 370 0 360Z" fill="#fde59a"/>
  <path d="M0 80 C120 40 260 30 330 70 C420 120 470 320 380 410 C310 470 220 420 140 380 C80 350 30 350 0 350Z" fill="#5a4a3e"/>
</svg>

<div class="abs story">
  <div class="kicker">BRAVA</div>
  <h2>Our Story</h2><span class="bar"></span>
  <p>Menc non elit libero. Quisque massa porta ut placerat len-tesque non diam. Nam convallis porta rhoncus. Maecenas varius eget turpis suscipit porta sapien tinc Mauris tempor libero fringilla orci vivrra faucibue fringilla orci vivrra faucibus. Integer ullamcorper erat in tellus efficitur.</p>
</div>
<div class="abs sign" role="img" aria-label="Owner's handwritten signature"></div>

<div class="abs tile" role="img" aria-label="Wood fired pizza on a board" style="left:88px;background:linear-gradient(135deg,#d8c49a,#a06b3a 55%,#4a3020)"><span>Dinner</span></div>
<div class="abs tile" role="img" aria-label="Tacos with red cabbage" style="left:607px;background:linear-gradient(135deg,#6a3a6e,#b9892e 50%,#cfcfcf)"><span>Takeout</span></div>

<h2 class="abs section-title" style="top:1652px">Customer Review</h2>
<span class="abs" style="left:562px;top:1708px;width:76px;height:4px;background:var(--yellow)"></span>

<div class="abs review" style="left:87px">
  <p>Etiam rhoncus maecenas tempus, tellus eget condim entum rhon cus sem quam semper libero amet adipisc ing sem neque sed ipsum nam quam nunc.</p><hr>
  <h4>Marisa</h4><small>Founder at Northwind</small><div class="stars">★★★★<i>★</i></div>
</div>
<div class="abs review" style="left:523px">
  <p>Etiam rhoncus maecenas tempus, tellus eget condim entum rhon cus sem quam semper libero amet adipisc ing sem neque sed ipsum nam quam nunc.</p><hr>
  <h4>Dario Kell</h4><small>Founder at Halvera</small><div class="stars">★★★★<i>★</i></div>
</div>
<div class="abs review" style="left:959px">
  <p>Etiam rhoncus maecenas tempus, tellus eget condim entum rhon cus sem quam semper libero amet adipisc ing sem neque sed ipsum nam quam nunc.</p><hr>
  <h4>Tomas Rylen</h4><small>Founder at Copperline</small><div class="stars">★★★★<i>★</i></div>
</div>
<div class="abs avatar" role="img" aria-label="Reviewer portrait" style="left:117px;background:radial-gradient(circle,#c99a7a,#8a5a4a)"></div>
<div class="abs avatar" role="img" aria-label="Reviewer portrait" style="left:553px;background:radial-gradient(circle,#d88070,#2fb5c8 70%)"></div>
<div class="abs avatar" role="img" aria-label="Reviewer portrait" style="left:990px;background:radial-gradient(circle,#e0a030,#555 70%)"></div>
<div class="abs dots"><b class="on"></b><b></b><b></b></div>

<h2 class="abs section-title" style="top:2166px">@Brava.Linwell</h2>
<span class="abs" style="left:562px;top:2222px;width:76px;height:4px;background:var(--yellow)"></span>

<div class="abs insta" role="img" aria-label="Grilled sandwich" style="left:88px;background:linear-gradient(135deg,#e6c46a,#b07a4a)"></div>
<div class="abs insta" role="img" aria-label="Guest with a plate of food" style="left:295px;background:linear-gradient(135deg,#8a6a5a,#d7b08a)"></div>
<div class="abs insta" role="img" aria-label="Tacos on a dark plate" style="left:501px;background:linear-gradient(135deg,#4a4a4a,#8a5a7a 50%,#c9a050)"></div>
<div class="abs insta" role="img" aria-label="Featured dish" style="left:707px;background:var(--yellow)"></div>
<div class="abs insta" role="img" aria-label="Colourful patio" style="left:913px;background:linear-gradient(180deg,#d85a3a,#c98a4a 60%,#a86a3a)"></div>

<div class="abs map" role="img" aria-label="Street map showing the restaurant location"></div>

<svg class="abs" style="left:0;top:2920px" width="1200" height="483" viewBox="0 0 1200 483" preserveAspectRatio="none">
  <path d="M0 90 C200 40 600 -10 1200 20 L1200 483 L0 483Z" fill="#000"/>
  <path d="M0 88 C200 38 600 -12 1200 18 L1200 8 C700 -10 260 20 0 88Z" fill="#fcd22c"/>
</svg>

<div class="abs flogo"><b>BRAVA</b><span>Stone Oven Kitchen</span></div>
<div class="abs footer-col" style="left:367px"><h3>Useful Links</h3>Menu<br>Gift Cards<br>Reservations<br>Take Out<br>Contact Us</div>
<div class="abs footer-col" style="left:616px;line-height:23px"><h3 style="line-height:26px">Dining Hours</h3>Courtyard is open<br>Thursday to Sunday<br>12:00pm – 9:00pm<h3 style="margin-top:8px;line-height:26px">Pickup &amp; Kitchen Hours</h3>Thursday to Sunday<br>12:00pm – 8:00pm</div>
<div class="abs footer-col" style="left:917px;line-height:20px"><h3 style="line-height:26px">Get In Touch</h3>
  <span style="color:var(--yellow)">●</span> 48 Alder Street<br>&nbsp;&nbsp;&nbsp;&nbsp;Linwell, ON<br>
  <span style="color:var(--yellow)">✆</span> 555-014-2290<br>
  <span style="color:var(--yellow)">✉</span> hello@bravalinwell.example
  <div class="social"><b></b><b></b><b></b><b></b></div>
</div>
<div class="abs rule"></div>
<div class="abs copy">Copyright © 2021 Brava</div>
<div class="abs totop"><svg width="32" height="32" viewBox="0 0 32 32"><path d="M12 18l4-4 4 4" fill="none" stroke="#111" stroke-width="1.5"/></svg></div>
</body>
</html>
```